Bed Company needs business card

Hello, we are a bed company that makes specialized magnets for beds. We are an alternative healing company. I need a modern and upscale business card. Please incorporate my logo for the card.

Accepted file formats are AI, EPS, and Press-Ready PDFS.

Please include all fonts or convert them to outlines regardless of file type.

If you are designing the card in Photoshop the file Must be 1200dpi.

I am open to anything for the business card.  I really like all of your designs and if you want to change the color of the logo, you can.  I will be making the final selection by Friday.  Thank You for all of your designs.  Feel Free to submit different color logos if you want.  

Reason: I will make a decision Final on Friday April 20th. 2012. Good Luck and Thank you all for the designs.

Target Market(s)

My target Market is people, who are looking for alternative healing.

Industry/Entity Type

Business

Requirements
Must have
• My logo must be incorporated. The front card must have

Name
Job Title

Address
Work
Cell
Fax
email
web

Just put in fake info for the card.

The back of the card. I want the logo on the back with color. I just want it to look modern and cool.

```html
<!DOCTYPE html>
<html lang="en">
<head>
<meta charset="utf-8">
<title>Restwell Field – Business Card</title>
<link href="https://fonts.googleapis.com/css2?family=Open+Sans:wght@300;400;700&display=swap" rel="stylesheet">
<style>
  :root {
    --backdrop: #e9e6e1;
    --card: #ffffff;
    --card-edge: #dcdcdc;
    --green: #1f7a35;
    --green-bright: #2f9a3f;
    --lime: #8cc63f;
    --ink: #333333;
    --ink-soft: #777777;
    --navy: #1f3a5a;
  }
  html, body {
    margin: 0;
    padding: 0;
    width: 1200px;
    height: 923px;
    overflow: hidden;
    background: var(--backdrop);
    font-family: "Open Sans", Arial, sans-serif;
  }
  .stage {
    position: relative;
    width: 1200px;
    height: 923px;
    display: flex;
    align-items: center;
    justify-content: center;
    gap: 50px;
  }
  .card {
    position: relative;
    width: 525px;
    height: 300px;
    background: var(--card);
    border-radius: 22px;
    box-shadow: 0 2px 0 var(--card-edge), 0 12px 30px rgba(0,0,0,0.18);
    overflow: hidden;
  }
  .brand {
    display: flex;
    align-items: center;
    gap: 10px;
  }
  .brand-mark {
    width: 26px;
    height: 26px;
    background: var(--green-bright);
  }
  .brand-name {
    font-weight: 700;
    color: var(--green-bright);
    font-size: 34px;
    line-height: 1;
    letter-spacing: -0.5px;
  }
  .brand-tagline {
    font-weight: 400;
    color: var(--green-bright);
    font-size: 12px;
    letter-spacing: 1.5px;
    margin: 4px 0 0 36px;
  }

  /* back card */
  .card-back .brand-block {
    position: absolute;
    left: 50%;
    top: 110px;
    transform: translateX(-50%);
    white-space: nowrap;
  }
  .card-back .brand-name { font-size: 26px; }
  .card-back .brand-mark { width: 20px; height: 20px; }
  .card-back .brand-tagline { font-size: 9px; margin-left: 30px; }
  .card-back .web {
    position: absolute;
    left: 0;
    right: 0;
    top: 186px;
    text-align: center;
    font-size: 12px;
    color: var(--ink);
  }

  /* front card */
  .card-front .swoosh {
    position: absolute;
    inset: 0;
  }
  .card-front .person {
    position: absolute;
    right: 28px;
    top: 24px;
    text-align: right;
  }
  .person-name {
    font-size: 17px;
    color: var(--navy);
    line-height: 1.1;
  }
  .person-role {
    font-size: 11px;
    color: var(--ink-soft);
  }
  .card-front .brand-block {
    position: absolute;
    left: 30px;
    top: 96px;
  }
  .contact {
    position: absolute;
    left: 30px;
    top: 170px;
    margin: 0;
    padding: 0;
    list-style: none;
    font-size: 12px;
    font-weight: 300;
    color: var(--ink);
    line-height: 1.45;
  }
  .card-front .web {
    position: absolute;
    right: 40px;
    bottom: 22px;
    font-size: 12px;
    color: #ffffff;
  }
</style>
</head>
<body>
<main class="stage">
  <section class="card card-back" aria-label="Card back">
    <div class="brand-block">
      <div class="brand">
        <span class="brand-mark"></span>
        <span class="brand-name">Restwell Field</span>
      </div>
      <div class="brand-tagline">Alternative Healing</div>
    </div>
    <div class="web">www.restwellfield.com</div>
  </section>

  <section class="card card-front" aria-label="Card front">
    <svg class="swoosh" width="525" height="300" viewBox="0 0 525 300" aria-hidden="true">
      <path d="M0 300 L0 292 C170 300 380 250 525 150 L525 300 Z" fill="var(--lime)"/>
      <path d="M0 300 C190 304 400 262 525 168 L525 300 Z" fill="#ffffff"/>
      <path d="M40 300 C230 298 420 258 525 182 L525 300 Z" fill="var(--green)"/>
    </svg>
    <div class="person">
      <div class="person-name">Your Name</div>
      <div class="person-role">Position</div>
    </div>
    <div class="brand-block">
      <div class="brand">
        <span class="brand-mark"></span>
        <span class="brand-name">Restwell Field</span>
      </div>
      <div class="brand-tagline">Alternative Healing</div>
    </div>
    <ul class="contact">
      <li>P: +(555)555-5555</li>
      <li>F: +(555)555-5555</li>
      <li>E: info@restwellfield.com</li>
      <li>#1321, Your Street, Your Location</li>
      <li>Your Town, Your Country</li>
    </ul>
    <div class="web">www.restwellfield.com</div>
  </section>
</main>
</body>
</html>
```